依頼概要
■依頼の目的/概要
2022年3月に港みらい展示館で開催される展示会「部品工作総合展」に芦野市・芦野商工会議所・芦野市内製造業6社で合同出展します。その際に配布するノベルティとしてオリジナル紙バッグを作成し、ブース来場者に配布するにあたり、デザインを募集します。

■依頼詳細
芦野市・芦野商工会議所が共同で立ち上げている組織「産業支援拠点芦野LINK」を中心に、金属加工やプラスチック加工、センサー製造、製造ラインの最速設計設置、基板修理など、様々な技術を持つ芦野市内の製造業6社の製品・サービスをPRするため、バッグを配布し、それを携帯した方が広告塔となって集客を行うことでブースへの集客を狙います。
6社が「何をできるのか」をキャッチコピーに表現し、一目で見てわかるようにします。
また、バッグデザインをブース装飾にも使うことで、統一感を出し、バッグのイメージを焼きつけた来場者(全国製造業企業の担当者)が、ブースを見つけやすいようにします。

デザインはバッグ両面のデザインをセットとして2案の作成をお願いします。

(1)表面:芦野市・芦野商工会議所(産業支援拠点 芦野LINK)、ブース番号
裏面:参加企業6社名、6社のキャッチコピーを配置したもの、ブース番号
(2)表面:芦野市・芦野商工会議所(産業支援拠点 芦野LINK)と参加企業6社のうち3社の社名・キャッチコピーを配置したもの、ブース番号
裏面:芦野市・芦野商工会議所(産業支援拠点 芦野LINK)と(3)に掲載以外の3社の社名・キャッチコピーを配置したもの、ブース番号

なお、ブース番号と各社キャッチコピーは強調して表記、企業名の表記は最小限の大きさでお願いします。

■バッグに記載する内容
芦野市・芦野商工会議所(芦野LINKのロゴ添付)
ブース番号:東4ホール3-18
<以下6社の企業名とキャッチコピー>
ミツハラ㈱「光センサーで問題解決!」
㈱朝倉製作所「量産最速立上げ」
㈲辰巳工業「極上の金属加工を召し上がれ」
ベルモア丹波㈱「THE・樹脂加工!」
㈱サクモト「金属機械加工のお困りごと相談所」
VERITAS㈱「老朽化装置の基板修理」

■デザインを依頼するノベルティ詳細
ノベルティ:紙バッグ
片面サイズ:縦31cm×横42cm

■重視するポイント
・集客力のあるデザイン
・バッグを持ちたくなる格好良いデザイン
・一目で見て、6社で何ができるかわかるデザイン
・ブース番号がすぐに認識できるデザイン

■決定後の納品方法
イラストレーター ver.CS 6 で編集可能なファイル形式で納品のこと。
芦野LINKのロゴですが、jpegデータに加えて、pdfデータも提供します。
芦野LINKのロゴ複数の形式のデータを掲載します。
■ 選んだ理由

キャッチコピーが目立つ配置、芦野LINKのロゴの配色を効果的に使いながら、独自のキャラクターによりオリジナリティも出ていて、硬いイメージになりがちな展示会のイメージとは違った雰囲気で逆に目立つと考え、採用させていただきました。また、修正依頼のレスポンスも早く、安心できました。

■ 提案者全員のお礼・コメント

短期間にたくさんのご提案をいただき、誠にありがとうございます。甲乙つけがたいデザインを提案いただき、選定も非常に難航しました。また機会がありましたら、ぜひご参加いただきたく存じます。

```html
<!DOCTYPE html>
<html lang="ja">
<head>
<meta charset="utf-8">
<title>Plan A — 芦野LINK 紙バッグ</title>
<link rel="stylesheet" href="https://fonts.googleapis.com/css2?family=Noto+Sans+JP:wght@400;500;700&family=Noto+Serif:wght@400&display=swap">
<style>
  :root{
    --paper:#ffffff;
    --board:#808080;
    --label:#4a4646;
    --bag:#363131;
    --blue:#2f86c1;
    --green:#7aae3a;
    --white:#ffffff;
  }
  *{margin:0;padding:0;box-sizing:border-box}
  html,body{width:1200px;height:1200px;overflow:hidden;background:var(--paper)}
  body{position:relative;font-family:"Noto Sans JP",sans-serif}

  .plan-title{position:absolute;right:48px;top:22px;font-family:"Noto Serif",serif;font-size:150px;font-weight:400;color:#333;line-height:1;letter-spacing:2px}

  .board{position:absolute;left:10px;top:214px;width:1180px;height:980px;background:var(--board)}
  .stage{position:absolute;background:#f3f3f3}
  .stage-front{left:10px;top:238px;width:588px;height:590px}
  .stage-back{left:598px;top:588px;width:592px;height:606px}

  .side-label{position:absolute;background:var(--label);color:var(--white);font-family:"Noto Serif",serif;font-size:50px;display:flex;align-items:center;justify-content:center;width:282px;height:82px}
  .label-front{left:600px;top:240px}
  .label-back{left:318px;top:1080px}

  .bag{position:absolute;width:540px;height:400px;background:var(--bag);overflow:hidden}
  .bag-front{left:34px;top:333px}
  .bag-back{left:624px;top:691px}
  .handle{position:absolute;top:0;width:46px;height:10px;border:3px solid #1d1a1a;border-top:none;border-radius:0 0 6px 6px}
  .bag-front .handle{left:247px}
  .bag-back .handle{left:247px}

  /* front */
  .band{position:absolute}
  .front-blue-a{left:0;top:0;width:540px;height:40px;background:var(--blue)}
  .front-blue-b{left:0;top:40px;width:300px;height:90px;background:var(--blue)}
  .front-blue-c{left:200px;top:130px;width:100px;height:45px;background:var(--blue)}
  .front-green-a{left:0;top:235px;width:300px;height:55px;background:var(--green)}
  .front-green-b{left:0;top:335px;width:300px;height:55px;background:var(--green)}

  .front-copy{position:absolute;left:312px;top:68px;width:215px}
  .org-name{color:var(--blue);font-weight:700;font-size:34px;line-height:1.12;letter-spacing:3px}
  .hub-label{color:var(--white);font-size:10px;letter-spacing:5px;margin-top:8px}
  .hub-name{color:var(--white);font-weight:500;font-size:24px;letter-spacing:3px;line-height:1.3}
  .hub-tagline{color:var(--white);font-size:9px;letter-spacing:2px;padding-bottom:6px;border-bottom:1px solid var(--white)}
  .booth{color:var(--green);font-weight:500;font-size:32px;letter-spacing:8px;line-height:1.05;margin-top:8px;border-left:2px solid var(--white);padding-left:6px}

  /* back */
  .offer{position:absolute;left:0;width:470px;height:40px;display:flex;align-items:center;justify-content:space-between;padding:0 14px 0 18px;color:var(--white)}
  .offer.blue{background:var(--blue)}
  .offer.green{background:var(--green)}
  .offer-copy{font-weight:700;font-size:20px;letter-spacing:1px;white-space:nowrap}
  .offer-maker{font-size:9px;align-self:flex-end;padding-bottom:3px;white-space:nowrap}
  .offer.last{background:none}
  .booth-vertical{position:absolute;right:-150px;top:180px;width:340px;transform:rotate(-90deg);color:var(--white);font-weight:500;font-size:30px;letter-spacing:5px;text-align:center;white-space:nowrap}
</style>
</head>
<body>
  <h1 class="plan-title">Plan A</h1>

  <div class="board"></div>
  <div class="stage stage-front"></div>
  <div class="stage stage-back"></div>

  <div class="side-label label-front">Front</div>
  <div class="side-label label-back">Back</div>

  <section class="bag bag-front" aria-label="バッグ表面">
    <div class="handle"></div>
    <div class="band front-blue-a"></div>
    <div class="band front-blue-b"></div>
    <div class="band front-blue-c"></div>
    <div class="band front-green-a"></div>
    <div class="band front-green-b"></div>
    <div class="front-copy">
      <p class="org-name">芦野市・<br>芦野商工<br>会議所</p>
      <p class="hub-label">産業支援拠点</p>
      <p class="hub-name">芦野LINK</p>
      <p class="hub-tagline">広がる・生まれる・進化する</p>
      <p class="booth">EAST<br>4HALL<br>3-18</p>
    </div>
  </section>

  <section class="bag bag-back" aria-label="バッグ裏面">
    <div class="handle"></div>
    <div class="offer blue" style="top:24px"><span class="offer-copy">光センサーで問題解決！</span><span class="offer-maker">ミツハラ㈱</span></div>
    <div class="offer green" style="top:84px"><span class="offer-copy">量産最速立上げ</span><span class="offer-maker">㈱朝倉製作所</span></div>
    <div class="offer blue" style="top:144px"><span class="offer-copy">極上の金属加工を召し上がれ</span><span class="offer-maker">㈲辰巳工業</span></div>
    <div class="offer green" style="top:204px"><span class="offer-copy">THE・樹脂加工！</span><span class="offer-maker">ベルモア丹波㈱</span></div>
    <div class="offer blue" style="top:264px"><span class="offer-copy">金属機械加工のお困りごと相談所</span><span class="offer-maker">㈱サクモト</span></div>
    <div class="offer green" style="top:324px"><span class="offer-copy">老朽化装置の基板修理</span><span class="offer-maker">VERITAS㈱</span></div>
    <p class="booth-vertical">EAST 4 HALL 3-18</p>
  </section>
</body>
</html>
```